New Business Card

We need to refresh our business cards. We designed these ourselves and we have no graphic design experience. We would like to find a new business card design that is professional and unique. We are an auto finance company. Feel free to play with the logo, but we would like to keep the eye very present on the card. Our corporate colors are green, grey, and white.
Green - RGB - 168,215,27; HEX - #AADD22
Grey - RGB - 196,196,196; HEX - #C4C4C4
Updates
Need to upload the vector file to finalize the project. The last logo was for a jpeg that didn't stretch well.
Industry/Entity Type
Financial Service
Contact Information for Business Card
Honestly don't know...I need your help!

```html
<!DOCTYPE html>
<html lang="en">
<head>
<meta charset="utf-8">
<title>Brightlane Capital – Business Card</title>
<link rel="stylesheet" href="https://fonts.googleapis.com/css2?family=Roboto+Condensed:wght@300;400;700&display=swap">
<style>
  :root {
    --green: #aadd22;
    --grey: #c4c4c4;
    --charcoal: #3e3e40;
    --white: #ffffff;
    --ink: #2b2b2d;
    --muted: #777779;
    --backdrop: #e9e8e5;
  }
  * { box-sizing: border-box; margin: 0; padding: 0; }
  html, body { width: 1200px; height: 891px; overflow: hidden; }
  body {
    background: var(--backdrop);
    font-family: "Roboto Condensed", sans-serif;
    display: flex;
    align-items: center;
    justify-content: center;
    gap: 90px;
  }
  .card {
    position: relative;
    width: 343px;
    height: 600px;
    overflow: hidden;
    box-shadow: 0 10px 28px rgba(0,0,0,0.18);
  }
  .card--front { background: var(--charcoal); }
  .card--back { background: var(--white); }
  .card__crest { position: absolute; inset: 0; width: 343px; height: 600px; }
  .brand {
    position: absolute;
    top: 118px;
    left: 0;
    width: 343px;
    display: flex;
    flex-direction: column;
    align-items: center;
    gap: 16px;
  }
  .card--back .brand { top: 100px; }
  .brand__mark {
    width: 58px; height: 58px;
    border-radius: 50%;
    background: var(--grey);
  }
  .brand__name {
    color: var(--green);
    font-weight: 700;
    font-size: 30px;
    letter-spacing: 0.5px;
    white-space: nowrap;
  }
  .person {
    position: absolute;
    left: 40px;
    top: 400px;
    padding-left: 14px;
  }
  .person::before {
    content: "";
    position: absolute;
    left: 0; top: 6px;
    width: 4px; height: 40px;
    background: var(--green);
  }
  .person__name { font-size: 22px; color: var(--ink); text-transform: uppercase; }
  .person__name b { font-weight: 700; }
  .person__name span { font-weight: 300; }
  .person__title { font-size: 13px; font-weight: 300; color: var(--muted); text-transform: uppercase; }
  .contacts {
    position: absolute;
    left: 54px;
    top: 472px;
    width: 260px;
    list-style: none;
    display: flex;
    flex-direction: column;
    gap: 10px;
  }
  .contacts li {
    display: flex;
    align-items: center;
    gap: 8px;
    font-size: 13px;
    font-weight: 300;
    color: var(--ink);
    white-space: nowrap;
  }
  .contacts svg { width: 13px; height: 13px; flex: none; fill: var(--green); }
</style>
</head>
<body>

<section class="card card--front" aria-label="Card front">
  <svg class="card__crest" viewBox="0 0 343 600" aria-hidden="true">
    <rect x="14" y="0" width="8" height="300" fill="var(--green)"/>
    <rect x="24" y="0" width="5" height="300" fill="var(--grey)"/>
    <rect x="321" y="0" width="8" height="300" fill="var(--green)"/>
    <rect x="314" y="0" width="5" height="300" fill="var(--grey)"/>
    <polygon points="38,-6 305,-6 305,300 171.5,395 38,300" fill="var(--charcoal)" stroke="var(--grey)" stroke-width="6"/>
  </svg>
  <div class="brand">
    <span class="brand__mark"></span>
    <span class="brand__name">Brightlane Capital</span>
  </div>
</section>

<section class="card card--back" aria-label="Card back">
  <svg class="card__crest" viewBox="0 0 343 600" aria-hidden="true">
    <rect x="14" y="0" width="8" height="300" fill="var(--green)"/>
    <rect x="24" y="0" width="5" height="300" fill="var(--grey)"/>
    <rect x="321" y="0" width="8" height="300" fill="var(--green)"/>
    <rect x="314" y="0" width="5" height="300" fill="var(--grey)"/>
    <polygon points="38,-6 305,-6 305,280 171.5,365 38,280" fill="var(--charcoal)" stroke="var(--grey)" stroke-width="6"/>
  </svg>
  <div class="brand">
    <span class="brand__mark"></span>
    <span class="brand__name">Brightlane Capital</span>
  </div>

  <div class="person">
    <p class="person__name"><b>Name</b> <span>Name</span></p>
    <p class="person__title">Job Title</p>
  </div>

  <ul class="contacts">
    <li>
      <svg viewBox="0 0 24 24"><path d="M6.6 10.8a15.1 15.1 0 0 0 6.6 6.6l2.2-2.2a1 1 0 0 1 1-.25 11.4 11.4 0 0 0 3.6.57 1 1 0 0 1 1 1V20a1 1 0 0 1-1 1A17 17 0 0 1 3 4a1 1 0 0 1 1-1h3.5a1 1 0 0 1 1 1c0 1.25.2 2.45.57 3.57a1 1 0 0 1-.25 1z"/></svg>
      000-123-456-789
    </li>
    <li>
      <svg viewBox="0 0 24 24"><path d="M2 5h20v14H2z M4 7v.5l8 5 8-5V7l-8 5z" fill-rule="evenodd"/></svg>
      yourmail@mailhost.com
    </li>
    <li>
      <svg viewBox="0 0 24 24"><path d="M12 2a10 10 0 1 0 0 20 10 10 0 0 0 0-20zm6.9 6h-3a15 15 0 0 0-1.3-4A8 8 0 0 1 18.9 8zM12 4c.8 1.2 1.5 2.5 1.9 4h-3.8c.4-1.5 1.1-2.8 1.900-4zM4.3 14a8 8 0 0 1 0-4h3.4a16 16 0 0 0 0 4zm.8 2h3a15 15 0 0 0 1.3 4A8 8 0 0 1 5.1 16zm3-8h-3a8 8 0 0 1 4.3-4 15 15 0 0 0-1.3 4zM12 20c-.8-1.2-1.5-2.5-1.9-4h3.8c-.4 1.5-1.1 2.8-1.9 4zm2.3-6H9.7a14 14 0 0 1 0-4h4.6a14 14 0 0 1 0 4zm.3 6a15 15 0 0 0 1.3-4h3a8 8 0 0 1-4.3 4zm1.7-6a16 16 0 0 0 0-4h3.4a8 8 0 0 1 0 4z"/></svg>
      www.yourwebsite.com
    </li>
    <li>
      <svg viewBox="0 0 24 24"><path d="M12 3 2 12h3v8h5v-5h4v5h5v-8h3z"/></svg>
      your address here 1234 road, NY
    </li>
  </ul>
</section>

</body>
</html>
```